Quandoria Tours - Astronomy in the Kimberley

Quandoria Tours requires a web page to advertise astronomy tours in the East Kimberley, Australia. It needs the following tabs - Home, Tours, Astronomy Events, Gallery, Testimonials, Contacts.

It should target tourists to the Kimberley.
We are unsure of which colours to go with at the moment but we have included our logo if it helps.

It should be mobile and tablet friendly.

Target Market(s)

Families, +40, Tourist, hobby astronomists,

Industry/Entity Type

Events

Number of Pages Required

3 page

Colors
3377b5
ffffff

Requirements
Must have
• Home, Tours, Astronomy Events, Gallery, Calendar, Testimonials, Contacts.
• 'Quandoria Tours' logo
Nice to have
• Pictures of portable amateur telescopes. Pictures of Lake Kununurra or Wyndham.
Should not have
• Pictures of extremely large professional telescopes.

```html
<!DOCTYPE html>
<html lang="en">
<head>
<meta charset="utf-8">
<title>Quandoria Tours – Astronomy in the Kimberley</title>
<link href="https://fonts.googleapis.com/css2?family=Open+Sans:wght@300;400;600;700&family=Yellowtail&family=Lobster&display=swap" rel="stylesheet">
<style>
:root{
  --brand:#3377b5;
  --brand-dark:#2a6298;
  --white:#ffffff;
  --ink:#222222;
  --muted:#9a9a9a;
  --dark-btn:#3d3d3d;
  --nav-bg:rgba(230,232,236,0.92);
  --footer:#3a3a3a;
  --footer-line:#5a5a5a;
  --footer-base:#2a2a2a;
  --gold:#f3b33d;
  --offer:#e8531c;
}
*{box-sizing:border-box;margin:0;padding:0}
html,body{width:1200px;height:2961px;overflow:hidden}
body{position:relative;font-family:"Open Sans",Arial,sans-serif;color:var(--ink);background:var(--white)}
.abs{position:absolute}

/* hero */
.hero{position:absolute;left:0;top:0;width:1200px;height:687px;
  background:linear-gradient(180deg,#2e3a6a 0%,#7a4a6e 30%,#c46a5a 42%,#3a3458 58%,#1a2440 78%,#0e1a36 100%)}
.nav{position:absolute;left:100px;top:0;width:942px;height:67px;background:var(--nav-bg);display:flex}
.nav a{display:flex;align-items:center;justify-content:center;height:67px;font-size:17px;color:var(--brand);text-decoration:none;border-right:1px solid #c9ccd2}
.nav a.active{background:var(--brand);color:var(--white)}
.search{position:absolute;left:1042px;top:0;width:60px;height:67px;background:var(--brand);display:flex;align-items:center;justify-content:center}
.badge{position:absolute;left:493px;top:69px;width:214px;height:184px}
.badge-name{position:absolute;left:493px;top:150px;width:214px;text-align:center;color:var(--white);font-size:25px;font-weight:600;line-height:1.1}
.caption{position:absolute;left:158px;top:316px;width:859px;height:201px;background:rgba(20,22,40,0.45);text-align:center;color:var(--white)}
.caption h1{font-weight:400;font-size:40px;margin-top:22px;letter-spacing:1px;display:inline-block;border-bottom:2px solid rgba(255,255,255,.8);padding:0 6px 4px}
.caption p{font-size:12.5px;margin-top:12px}
.caption .btn{display:inline-block;margin-top:22px;border:1px solid var(--white);background:rgba(0,0,0,.35);padding:7px 22px;font-size:12px;color:var(--white)}
.arrow{position:absolute;top:389px;width:40px;height:40px;background:var(--brand);display:flex;align-items:center;justify-content:center}
.dots{position:absolute;left:568px;top:657px;display:flex;gap:6px}
.dots span{width:16px;height:16px;border-radius:50%;background:var(--white)}
.dots span.on{background:var(--brand)}

/* destinations */
.dest{position:absolute;top:775px;width:340px;text-align:center}
.dest .photo{width:148px;height:148px;border-radius:50%;margin:0 auto}
.dest h2{font-weight:400;font-size:42px;color:var(--brand);margin-top:26px;line-height:1}
.dest .from{font-size:14px;margin-top:12px}
.dest .price{font-size:33px;line-height:1.1}
.dest p{font-size:11px;color:#b2b2b2;line-height:20px;margin:14px auto 0;width:320px}
.more{display:inline-flex;margin-top:28px;height:38px}
.more .lbl{background:var(--brand);color:var(--white);font-size:11px;font-weight:600;padding:0 16px;display:flex;align-items:center}
.more .ic{width:38px;background:var(--dark-btn);display:flex;align-items:center;justify-content:center}
.more.dark .lbl,.more.dark .ic{background:var(--dark-btn)}

/* category */
.category{position:absolute;left:0;top:1289px;width:1200px;height:606px;background:var(--brand)}
.category h2{position:absolute;top:30px;width:100%;text-align:center;color:var(--white);font-weight:400;font-size:44px}
.tile{position:absolute;width:487px;height:212px;overflow:hidden}
.tile .script{position:absolute;left:28px;top:38px;font-family:"Yellowtail",cursive;color:var(--white);font-size:88px;line-height:1}
.tile .sub{position:absolute;left:30px;top:136px;color:var(--white);font-size:14px;letter-spacing:2px;font-weight:600}

/* news */
.news-title{position:absolute;top:1930px;width:100%;text-align:center;font-size:44px;font-weight:400}
.news{position:absolute;top:2014px;width:230px;text-align:center}
.date{width:118px;height:118px;border-radius:50%;border:2px solid var(--brand);margin:0 auto;overflow:hidden;position:relative;background:var(--white)}
.date .d{position:absolute;top:22px;width:100%;font-size:28px;color:var(--brand)}
.date .d b{font-weight:700}
.date .y{position:absolute;bottom:0;width:100%;height:38px;background:var(--brand);color:var(--white);font-weight:700;font-size:19px;line-height:34px}
.news h3{font-size:26px;font-weight:700;line-height:32px;margin-top:24px}
.news p{font-size:13.5px;color:var(--muted);margin-top:4px}
.news a{font-size:13.5px;color:var(--brand)}

/* offer banner */
.offer{position:absolute;left:99px;top:2347px;width:1002px;height:199px;
  background:linear-gradient(180deg,#6a5a8c 0%,#c98a86 45%,#f2a75a 80%,#e8894a 100%)}
.stamp{position:absolute;left:337px;top:14px;width:166px;height:166px;border-radius:50%;background:var(--white);border:4px solid #f2c27a;text-align:center}
.stamp .amt{font-size:44px;font-weight:700;color:var(--offer);margin-top:28px;line-height:1}
.stamp .off{font-size:19px;font-weight:700;color:#444;margin-top:8px;border-top:2px solid #ddd;display:inline-block;padding-top:4px}
.offer .t1{position:absolute;left:505px;top:40px;font-family:"Lobster",cursive;color:var(--gold);font-size:44px}
.offer .t2{position:absolute;left:505px;top:94px;font-family:"Lobster",cursive;color:var(--white);font-size:38px}
.offer .learn{position:absolute;right:0;bottom:0;width:160px;height:34px;background:var(--brand);color:var(--white);font-family:"Lobster",cursive;font-size:17px;display:flex;align-items:center;justify-content:center;clip-path:polygon(18% 0,100% 0,100% 100%,0 100%)}

/* footer */
.footer{position:absolute;left:0;top:2592px;width:1200px;height:316px;background:var(--footer);color:#d8d8d8;border-top:4px solid #555}
.footer h4{font-size:16px;font-weight:400;color:var(--white)}
.footer p{font-size:10.5px;line-height:20px}
.footer .rm{color:var(--brand);font-size:10.5px}
.links{list-style:none;margin-top:10px;width:318px}
.links li{font-size:10.5px;border-bottom:1px solid var(--footer-line);padding:3px 12px;line-height:16px}
.field{width:260px;height:28px;background:var(--white);font-size:10px;color:#999;padding:8px 12px;margin-top:10px}
.submit{display:inline-block;margin-top:14px;background:#111;color:var(--white);font-size:10px;font-weight:700;padding:7px 16px}
.base{position:absolute;left:0;top:2908px;width:1200px;height:53px;background:var(--footer-base);color:#bbb;font-size:10px;padding:21px 99px}
</style>
</head>
<body>

<header class="hero" role="img" aria-label="Harbour city skyline at sunset with an opera house and arch bridge reflected in the water">
  <nav class="nav">
    <a class="active" style="width:94px">Home</a>
    <a style="width:100px">Tours</a>
    <a style="width:186px">Astronomy Events</a>
    <a style="width:114px">Gallery</a>
    <a style="width:146px">Testimonials</a>
    <a style="width:118px;border-right:0">Contacts</a>
  </nav>
  <div class="search">
    <svg width="30" height="30" viewBox="0 0 30 30"><circle cx="12" cy="12" r="8.5" fill="none" stroke="#fff" stroke-width="3"/><line x1="18.5" y1="18.5" x2="27" y2="27" stroke="#fff" stroke-width="3.5" stroke-linecap="round"/></svg>
  </div>
  <svg class="badge" viewBox="0 0 214 184"><path d="M0 0H214V184L107 150L0 184Z" fill="#1f2233"/></svg>
  <div class="badge-name">Quandoria<br>tours</div>
  <div class="caption">
    <h1>HARBOUR NIGHTS</h1>
    <p>Lorem ipsum dolor sit amet conse ctetur adipiscing elit, sed do eiusmod tempor incididunt ut labore et dolore magna aliqua. Ut enim ad minim.</p>
    <span class="btn">Read More</span>
  </div>
  <div class="arrow" style="left:0"><svg width="14" height="20" viewBox="0 0 14 20"><path d="M11 2L3 10L11 18" fill="none" stroke="#fff" stroke-width="3"/></svg></div>
  <div class="arrow" style="left:1160px"><svg width="14" height="20" viewBox="0 0 14 20"><path d="M3 2L11 10L3 18" fill="none" stroke="#fff" stroke-width="3"/></svg></div>
  <div class="dots"><span class="on"></span><span></span><span></span></div>
</header>

<section>
  <div class="dest" style="left:85px">
    <div class="photo" role="img" aria-label="Overwater bungalows above a turquoise lagoon" style="background:radial-gradient(circle at 50% 30%,#9fd8ef,#25b6c4 55%,#1a8ea0)"></div>
    <h2>MALDIVES</h2><div class="from">FROM</div><div class="price">$ 2.100</div>
    <p>Mers cumi dia sed in lacus ut eniascet ingerto aliqt es site amet eismod ictor ut ligulate ameti dapibus ticdu nt etiam iusto dolor lissam comes cumi dia sed.</p>
    <span class="more"><span class="lbl">MORE INFO</span><span class="ic"><svg width="10" height="14" viewBox="0 0 10 14"><path d="M2 1L8 7L2 13" fill="none" stroke="#fff" stroke-width="2.5"/></svg></span></span>
  </div>
  <div class="dest" style="left:428px">
    <div class="photo" role="img" aria-label="Longtail boat on a beach beneath limestone cliffs" style="background:linear-gradient(180deg,#6fa9d8 0%,#9cc9e6 40%,#c59a5a 70%,#e2c79a 100%)"></div>
    <h2>THAILAND</h2><div class="from">FROM</div><div class="price">$ 1.899</div>
    <p>Mers cumi dia sed in lacus ut eniascet ingerto aliqt es site amet eismod ictor ut ligulate ameti dapibus ticdu nt etiam iusto dolor lissam comes cumi dia sed.</p>
    <span class="more"><span class="lbl">MORE INFO</span><span class="ic"><svg width="10" height="14" viewBox="0 0 10 14"><path d="M2 1L8 7L2 13" fill="none" stroke="#fff" stroke-width="2.5"/></svg></span></span>
  </div>
  <div class="dest" style="left:772px">
    <div class="photo" role="img" aria-label="Palm tree and boat on a white sand beach" style="background:linear-gradient(180deg,#4aa3db 0%,#8fd0ee 50%,#e9e3d2 80%,#f4efe2 100%)"></div>
    <h2>HAWAII</h2><div class="from">FROM</div><div class="price">$ 2.900</div>
    <p>Mers cumi dia sed in lacus ut eniascet ingerto aliqt es site amet eismod ictor ut ligulate ameti dapibus ticdu nt etiam iusto dolor lissam comes cumi dia sed.</p>
    <span class="more dark"><span class="ic"><svg width="10" height="14" viewBox="0 0 10 14"><path d="M2 1L8 7L2 13" fill="none" stroke="#fff" stroke-width="2.5"/></svg></span><span class="lbl" style="padding-left:4px">MORE INFO</span></span>
  </div>
</section>

<section class="category">
  <h2>Catagory</h2>
  <div class="tile" style="left:99px;top:116px" role="img" aria-label="Limestone cliff over calm sea" aria-describedby="c1"><div style="position:absolute;inset:0;background:linear-gradient(90deg,#8a6a58 0%,#a98a74 40%,#9fc2c6 60%,#5fa3a6 100%)"></div><div class="script" id="c1">summer</div><div class="sub">SALE</div></div>
  <div class="tile" style="left:614px;top:116px" role="img" aria-label="Resort pool above a rocky coast"><div style="position:absolute;inset:0;background:linear-gradient(135deg,#7fa6b8 0%,#6fb7c3 40%,#b79b86 70%,#d1b9a3 100%)"></div><div class="script">special</div><div class="sub">OFFERS</div></div>
  <div class="tile" style="left:99px;top:355px" role="img" aria-label="Family villa with tiled roof and pool"><div style="position:absolute;inset:0;background:linear-gradient(160deg,#c26a45 0%,#d58b62 35%,#6fb6b4 65%,#3f8f6a 100%)"></div><div class="script">family</div><div class="sub">TRAVEL</div></div>
  <div class="tile" style="left:614px;top:355px" role="img" aria-label="Iron lattice tower above a city park"><div style="position:absolute;inset:0;background:linear-gradient(180deg,#cfe0e6 0%,#a9bfc4 45%,#7d9a83 75%,#5f7f58 100%)"></div><div class="script">honeymoon</div><div class="sub">PACKAGES</div></div>
</section>

<section>
  <h2 class="news-title">NEWS</h2>
  <div class="news" style="left:104px"><div class="date"><div class="d"><b>6</b> Oct</div><div class="y">2015</div></div><h3>Etiam a odio nec</h3><p>Lorem ipsum dolor sit amet,</p><a>More info</a></div>
  <div class="news" style="left:361px"><div class="date"><div class="d"><b>6</b> Oct</div><div class="y">2015</div></div><h3>Lorem ipsum<br>dolor</h3><p>Lorem ipsum dolor sit amet,</p><a>More info</a></div>
  <div class="news" style="left:619px"><div class="date"><div class="d"><b>6</b> Oct</div><div class="y">2015</div></div><h3>Nulla nec ligula<br>risus</h3><p>Lorem ipsum dolor sit amet,</p><a>More info</a></div>
  <div class="news" style="left:876px"><div class="date"><div class="d"><b>29</b> Apr</div><div class="y">2015</div></div><h3>Stargazing Video</h3><p>Praesent sit amet ligula in ante</p><a>More info</a></div>
</section>

<aside class="offer" role="img" aria-label="Sunset beach with silhouetted palm trees">
  <div class="stamp"><div class="amt">$999</div><div class="off">20%OFF</div></div>
  <div class="t1">Punta Cana</div>
  <div class="t2">Luxe Destination Weddings</div>
  <div class="learn">learn more</div>
</aside>

<footer class="footer">
  <div class="abs" style="left:99px;top:24px;width:310px">
    <h4>ABOUT US</h4>
    <p style="margin-top:6px">Lorem ipsum dolor sit amet, consectetur adipiscing elit. Nunc non diam erat. In fringilla massa ut nisi ullamcorper pellentesque. Quisque non luctus sem.</p>
    <div class="rm">Read More »</div>
    <h4 style="margin-top:22px">BLOGS</h4>
    <p style="margin-top:6px;font-weight:700;color:#fff;line-height:14px">Post Title</p>
    <p style="font-size:8px;line-height:12px">Friday, 6th April 2015</p>
    <p>Lorem ipsum dolor sit amet, consectetur adipiscing elit. Nunc non diam erat. In fringilla massa ut nisi ullamcorper pellentesque.</p>
    <div class="rm">Read More »</div>
  </div>
  <div class="abs" style="left:442px;top:24px">
    <h4>LATEST NEWS</h4>
    <ul class="links">
      <li>Lorem ipsum dolor sit</li><li>Amet consectetur</li><li>Praesent vel sem id</li><li>Curabitur hendrerit est</li><li>Aliquam eget erat nec sapien</li><li>Cras id augue nunc</li><li>In nec justo non</li><li>Vivamus mollis enim ut</li><li>Curabitur hendrerit est</li>
    </ul>
  </div>
  <div class="abs" style="left:784px;top:24px;width:300px">
    <h4>NEWS LETTER</h4>
    <p style="margin-top:6px">Vestibulumaccumsan egestibulum eu justo convallis augue estas aenean elit intesque sed.</p>
    <div class="field">Name</div>
    <div class="field">Email</div>
    <span class="submit">SUBMIT</span>
    <h4 style="margin-top:18px">CONTACT US</h4>
    <p style="line-height:16px;margin-top:4px">Tel: xxxxx xxxxxxxxxx<br>Email: hello@quandoria-tours.example</p>
  </div>
</footer>
<div class="base">Copyright © 2015 · All Rights Reserved</div>

</body>
</html>
```